Herbal tea shop web designing - Brewvine

We need a business-charity purpose online shop selling premium herbal teas with a tagline "Healthy with a heart" where all the raw materials are being purchased from Indonesian local farmers in order to give them sustainable employment. Every 20% from the total amount of the customer's purchase from our website always goes back to their communities to help build better sanitation, education or whatever they need. We need page to blog too and another page for customers to interact and share their thought. we expect an eye catching simple earthy (maybe a bit rustic) design with some brush lettering font in some parts. Thank you.

Target Market(s)

-Tea Lovers
-Anyone with body weight issues or any health issues in general

Industry/Entity Type

Home Health Care

Number of Pages Required

5+ page

Font styles to use
Other font styles liked:
• brush lettering font in some parts

Requirements
Must have
• - Brush lettering font
• -Simple, a bit rustic design with some nice watercolor touch
• -Blogging Page
• -catchy yet fancy and elegant E-commerce page
Nice to have
• Well, I will let the designers use their skills and imaginations to the fullest.

```html
<!DOCTYPE html>
<html lang="en">
<head>
<meta charset="utf-8">
<title>Brewvine – Healthy with a heart</title>
<link href="https://fonts.googleapis.com/css2?family=Kaushan+Script&family=Open+Sans:wght@400;600;700;800&display=swap" rel="stylesheet">
<style>
:root{
  --paper:#e9d3ad;
  --paper-dark:#c9a06a;
  --ink:#2f2a26;
  --text:#5d5d5d;
  --muted:#9a9a9a;
  --orange:#f57c13;
  --orange-dark:#e06a07;
  --sky:#3fb6e8;
  --sky-soft:#bfe6f6;
  --sky-deep:#1d8fcf;
  --wood:#5a3622;
  --wood-dark:#3a2215;
  --white:#ffffff;
  --rose:#f3c9d4;
}
*{box-sizing:border-box;margin:0;padding:0}
html,body{width:1200px;height:2888px;overflow:hidden;background:var(--white)}
body{font-family:"Open Sans",Arial,sans-serif;color:var(--text)}
.page{position:relative;width:1200px;height:2888px;overflow:hidden;background:var(--white)}
.abs{position:absolute}
.script{font-family:"Kaushan Script",cursive}

/* header */
.hero{left:0;top:0;width:1200px;height:560px;
  background:radial-gradient(ellipse at 30% 40%,#f3e2c2 0%,var(--paper) 45%,var(--paper-dark) 100%)}
.topbar{left:0;top:0;width:1200px;height:30px}
.social-top{left:120px;top:9px;display:flex;gap:14px}
.social-top span{width:12px;height:12px;border-radius:50%;background:var(--ink);opacity:.75}
.account-links{right:120px;top:6px;display:flex;gap:22px;font-size:12px;color:var(--ink)}
.brand{left:120px;top:62px;font-weight:800;font-size:46px;color:var(--ink);letter-spacing:.5px}
.main-nav{left:462px;top:86px;display:flex;gap:34px;font-size:17px;font-weight:600;color:var(--ink)}
.cart{left:982px;top:78px;display:flex;align-items:center;gap:8px;font-size:14px;color:var(--ink)}
.cart i{display:block;width:38px;height:38px;border-radius:50%;background:var(--orange)}
.hero-title{left:120px;top:236px;font-size:56px;color:var(--ink);line-height:1}
.hero-sub{left:122px;top:310px;font-size:36px;color:var(--orange)}
.btn{display:inline-block;border-radius:26px;color:var(--white);font-weight:600;text-align:center}
.btn-orange{left:120px;top:388px;width:164px;height:48px;line-height:48px;background:var(--orange);font-size:17px}
.slider-dots{left:120px;top:490px;display:flex;gap:10px}
.slider-dots span{width:13px;height:13px;border-radius:50%;border:2px solid var(--ink)}
.slider-dots span.on{background:var(--ink)}
.photo-circle{border-radius:50%;border:8px solid var(--white);box-shadow:0 6px 18px rgba(0,0,0,.25)}
.hero-photo-main{left:800px;top:110px;width:330px;height:330px;
  background:radial-gradient(circle at 45% 40%,#b2453a,#6b2b22 60%,#3d1a12)}
.hero-photo-cup{left:660px;top:300px;width:250px;height:250px;
  background:radial-gradient(circle at 50% 45%,#f2c15b,#c9852b 50%,#6e6a3c)}
.hero-photo-small{left:690px;top:120px;width:150px;height:150px;
  background:radial-gradient(circle at 50% 50%,#e7d7a6,#b6874a)}

/* welcome */
.welcome-flowers{left:150px;top:600px;width:380px;height:400px;border-radius:50%;
  background:radial-gradient(circle at 50% 50%,#e0672c 0%,#f0c97d 22%,#f4eef6 42%,#9a8fd6 62%,rgba(90,150,90,.6) 75%,rgba(255,255,255,0) 80%)}
.welcome-title{left:722px;top:722px;font-size:40px;color:#6a6a6a}
.welcome-copy{left:722px;top:788px;width:400px;font-size:13.5px;line-height:22px;color:var(--muted)}
.btn-blue{background:var(--sky)}
.welcome-btn{left:722px;top:952px;width:140px;height:42px;line-height:42px;font-size:15px}

/* products */
.products-band{left:0;top:1060px;width:1200px;height:640px}
.products-title{left:0;top:1168px;width:1200px;text-align:center;font-size:36px;color:var(--ink)}
.products-grid{left:118px;top:1236px;display:flex;gap:18px}
.product-card{width:232px;height:322px;background:var(--white);box-shadow:0 3px 10px rgba(0,0,0,.12);padding:8px}
.product-photo{height:186px}
.product-name{margin:14px 6px 2px;font-size:15px;font-weight:700;color:var(--ink)}
.product-note{margin:0 6px;font-size:11px;color:var(--muted)}
.product-foot{display:flex;justify-content:space-between;align-items:center;margin:18px 6px 0}
.price{font-size:20px;font-weight:700;color:var(--sky-deep)}
.buy{width:88px;height:30px;line-height:30px;font-size:13px;background:var(--sky)}

/* features */
.feature-wrap{left:0;top:1680px;width:1200px;height:400px}
.feature{width:320px;height:320px;border-radius:50%;border:6px solid rgba(255,255,255,.9);
  box-shadow:0 4px 16px rgba(0,0,0,.2);display:flex;flex-direction:column;align-items:center;justify-content:center}
.feature-label{font-size:32px;color:var(--white);text-shadow:0 2px 6px rgba(0,0,0,.5)}
.feature-arrow{margin-top:18px;width:40px;height:40px}
.feature-1{left:130px;top:1712px;background:radial-gradient(circle at 50% 45%,#8f6a2c,#55421d 60%,#2f2410)}
.feature-2{left:440px;top:1712px;background:radial-gradient(circle at 50% 45%,#a35a3f,#6c3a2a 60%,#3a1e14)}
.feature-3{left:752px;top:1712px;background:radial-gradient(circle at 50% 45%,#7a5640,#4e3626 60%,#2a1c12)}

/* pledge */
.pledge{left:0;top:2080px;width:1200px;height:340px;
  background:linear-gradient(180deg,var(--wood) 0%,#6b4129 40%,var(--wood-dark) 100%)}
.pledge-text{left:150px;top:2184px;width:900px;text-align:center;font-size:25px;line-height:36px;color:var(--white)}

/* footer */
.footer{left:0;top:2420px;width:1200px;height:420px}
.footer-col{top:2508px}
.footer-col h3{font-size:21px;font-weight:600;color:var(--ink);margin-bottom:18px}
.footer-col li{list-style:none;font-size:12.5px;line-height:21px;color:var(--muted)}
.col-links{left:122px}
.col-resources{left:336px}
.col-blogs{left:520px;width:280px}
.col-news{left:836px;width:250px}
.blog-item{font-size:12px;line-height:18px;color:var(--muted);margin-bottom:14px}
.blog-item b{color:var(--text);font-weight:600}
.footer-social{left:336px;top:2692px;display:flex;gap:10px}
.footer-social span{width:26px;height:26px;border-radius:50%;background:var(--orange)}
.news-input{width:246px;height:34px;border:1px solid #d8d8d8;background:var(--white);font-size:12px;line-height:32px;padding-left:10px;color:#b0b0b0}
.news-btn{margin-top:12px;width:110px;height:32px;line-height:32px;border-radius:0;background:var(--orange);font-size:12px;font-weight:700}
.pay-cards{display:flex;gap:6px;margin-top:14px}
.pay-cards span{width:38px;height:24px;border-radius:3px;background:#dfe3e8;border:1px solid #c8cdd3}
.legal{left:0;top:2840px;width:1200px;height:48px;border-top:1px solid #ececec;text-align:center;line-height:48px;font-size:11px;color:var(--muted)}
</style>
</head>
<body>
<div class="page">

  <!-- Hero -->
  <section class="abs hero" aria-label="Hero"></section>
  <svg class="abs" style="left:0;top:500px" width="1200" height="70" viewBox="0 0 1200 70" aria-hidden="true">
    <path d="M0 40 L60 22 L110 38 L170 18 L240 42 L300 26 L360 46 L430 20 L500 40 L560 28 L640 48 L700 24 L780 44 L850 22 L920 40 L990 26 L1060 46 L1130 24 L1200 38 L1200 70 L0 70 Z" fill="#ffffff"/>
  </svg>

  <div class="abs topbar">
    <div class="abs social-top"><span></span><span></span><span></span><span></span></div>
    <div class="abs account-links"><span>My Account</span><span>Wishlist</span><span>Login</span><span>Sign up</span></div>
  </div>
  <div class="abs brand">Brewvine</div>
  <nav class="abs main-nav"><span>About Us</span><span>Our Product</span><span>Shop Now</span><span>Best Sellers</span></nav>
  <div class="abs cart"><i></i><span>0 items</span></div>

  <h1 class="abs hero-title script">Healthy with a heart</h1>
  <div class="abs hero-sub script">Try Herbal Teas</div>
  <a class="abs btn btn-orange">Shop Now ›</a>
  <div class="abs slider-dots"><span class="on"></span><span class="on"></span><span class="on"></span><span></span></div>

  <div class="abs photo-circle hero-photo-small" role="img" aria-label="Cup of herbal tea with leaves"></div>
  <div class="abs photo-circle hero-photo-main" role="img" aria-label="Dried rose and herbal tea blend"></div>
  <div class="abs photo-circle hero-photo-cup" role="img" aria-label="Glass cup of golden herbal tea with lemon"></div>

  <!-- Welcome -->
  <div class="abs" style="left:820px;top:860px;width:420px;height:280px;border-radius:50%;background:radial-gradient(ellipse,rgba(63,182,232,.35),rgba(63,182,232,0) 70%)" aria-hidden="true"></div>
  <div class="abs" style="left:-60px;top:760px;width:300px;height:260px;border-radius:50%;background:radial-gradient(ellipse,rgba(243,201,212,.6),rgba(243,201,212,0) 70%)" aria-hidden="true"></div>
  <div class="abs welcome-flowers" role="img" aria-label="Cup of tea surrounded by fresh herbs and flowers"></div>
  <h2 class="abs welcome-title script">Welcome to Brewvine</h2>
  <p class="abs welcome-copy">Every blend we pour is grown by local farming families in Indonesia. We buy their herbs at fair prices so they can count on steady work season after season. Each cup you enjoy helps a village build cleaner water, brighter schools and healthier homes. Sip slowly and share the warmth with everyone around you.</p>
  <a class="abs btn btn-blue welcome-btn">Read More ›</a>

  <!-- Products -->
  <svg class="abs products-band" width="1200" height="640" viewBox="0 0 1200 640" aria-hidden="true">
    <defs>
      <linearGradient id="waterBlue" x1="0" y1="0" x2="1" y2="1">
        <stop offset="0" stop-color="#bfe6f6"/>
        <stop offset=".5" stop-color="#4fbcec"/>
        <stop offset="1" stop-color="#1d8fcf"/>
      </linearGradient>
    </defs>
    <path d="M0 60 C200 10 420 80 640 40 C860 0 1020 60 1200 30 L1200 560 C1000 610 820 540 600 590 C380 640 200 570 0 610 Z" fill="url(#waterBlue)" opacity=".85"/>
    <path d="M0 520 C220 470 420 560 640 520 C880 480 1040 540 1200 500" stroke="#ffffff" stroke-width="14" fill="none" opacity=".9"/>
  </svg>
  <h2 class="abs products-title script">Our Products</h2>
  <div class="abs products-grid">
    <article class="product-card">
      <div class="product-photo" role="img" aria-label="Glass teapot of amber herbal tea" style="background:linear-gradient(160deg,#6b5133,#c98b3c 55%,#3b2c1c)"></div>
      <div class="product-name">Product Name</div>
      <div class="product-note">Calming leaf blend</div>
      <div class="product-foot"><span class="price">$12.99</span><a class="btn buy">Buy Now</a></div>
    </article>
    <article class="product-card">
      <div class="product-photo" role="img" aria-label="Cup of green herbal tea with mint" style="background:linear-gradient(160deg,#7e8a3a,#d9c85a 55%,#4c5a22)"></div>
      <div class="product-name">Product Name</div>
      <div class="product-note">Fresh mint infusion</div>
      <div class="product-foot"><span class="price">$12.99</span><a class="btn buy">Buy Now</a></div>
    </article>
    <article class="product-card">
      <div class="product-photo" role="img" aria-label="Cup of golden tea on a saucer" style="background:linear-gradient(160deg,#c7a46a,#f0cc74 55%,#8d6d3c)"></div>
      <div class="product-name">Product Name</div>
      <div class="product-note">Golden ginger brew</div>
      <div class="product-foot"><span class="price">$12.99</span><a class="btn buy">Buy Now</a></div>
    </article>
    <article class="product-card">
      <div class="product-photo" role="img" aria-label="Mug of chamomile tea with dried flowers" style="background:linear-gradient(160deg,#a0835a,#e6c88b 55%,#5e4630)"></div>
      <div class="product-name">Product Name</div>
      <div class="product-note">Chamomile bloom tea</div>
      <div class="product-foot"><span class="price">$12.99</span><a class="btn buy">Buy Now</a></div>
    </article>
  </div>

  <!-- Features -->
  <div class="abs" style="left:0;top:1720px;width:380px;height:320px;border-radius:50%;background:radial-gradient(ellipse,rgba(243,201,212,.7),rgba(243,201,212,0) 70%)" aria-hidden="true"></div>
  <div class="abs" style="left:860px;top:1700px;width:380px;height:340px;border-radius:50%;background:radial-gradient(ellipse,rgba(63,182,232,.35),rgba(63,182,232,0) 70%)" aria-hidden="true"></div>
  <div class="abs feature feature-1" role="img" aria-label="Loose leaf tea in a bowl">
    <span class="feature-label script">Best Sellers</span>
    <svg class="feature-arrow" viewBox="0 0 40 40" aria-hidden="true"><circle cx="20" cy="20" r="18" fill="none" stroke="#fff" stroke-width="2"/><path d="M17 13 L24 20 L17 27" stroke="#fff" stroke-width="2.5" fill="none"/></svg>
  </div>
  <div class="abs feature feature-2" role="img" aria-label="Two cups of red herbal tea">
    <span class="feature-label script">Why Us</span>
    <svg class="feature-arrow" viewBox="0 0 40 40" aria-hidden="true"><circle cx="20" cy="20" r="18" fill="none" stroke="#fff" stroke-width="2"/><path d="M17 13 L24 20 L17 27" stroke="#fff" stroke-width="2.5" fill="none"/></svg>
  </div>
  <div class="abs feature feature-3" role="img" aria-label="Assorted dried herbs and spices">
    <span class="feature-label script">Healthy &amp; Natural</span>
    <svg class="feature-arrow" viewBox="0 0 40 40" aria-hidden="true"><circle cx="20" cy="20" r="18" fill="none" stroke="#fff" stroke-width="2"/><path d="M17 13 L24 20 L17 27" stroke="#fff" stroke-width="2.5" fill="none"/></svg>
  </div>

  <!-- Pledge -->
  <section class="abs pledge" role="img" aria-label="Wooden table with scattered dried tea leaves"></section>
  <p class="abs pledge-text">We give 20% from the total amount of the customer's purchase from our website always goes back to their communities to help build better sanitation, education or whatever they need</p>

  <!-- Footer -->
  <div class="abs footer" aria-hidden="true" style="background:radial-gradient(ellipse at 85% 0%,rgba(63,182,232,.3),rgba(63,182,232,0) 45%),radial-gradient(ellipse at 15% 0%,rgba(63,182,232,.2),rgba(63,182,232,0) 40%)"></div>

  <div class="abs footer-col col-links">
    <h3>Quick Links</h3>
    <ul><li>About Brewvine</li><li>Business services</li><li>Pickup from your door</li><li>Jobs</li><li>Shipping Information</li></ul>
  </div>
  <div class="abs footer-col col-resources">
    <h3>Resources</h3>
    <ul><li>Privacy policy</li><li>Security Classifieds</li><li>Contact Us</li><li>Privacy Policy</li></ul>
  </div>
  <div class="abs footer-social"><span></span><span></span><span></span><span></span></div>
  <div class="abs footer-col col-blogs">
    <h3>Latest Blogs</h3>
    <p class="blog-item"><b>Meet our farmers</b> in the highlands who grow every leaf with care and patience.</p>
    <p class="blog-item"><b>Brewing tips</b> for a smoother cup: water heat, steep time and the right pot.</p>
  </div>
  <div class="abs footer-col col-news">
    <h3>Join Newsletter</h3>
    <div class="news-input">Email address</div>
    <a class="btn news-btn">SUBSCRIBE</a>
    <div class="pay-cards"><span></span><span></span><span></span><span></span><span></span></div>
  </div>

  <div class="abs legal">© 2017 Company Name. All rights reserved. Terms of use</div>
</div>
</body>
</html>
```